Travel Company is looking for a STAND OUT Business Card

I need a unique Business Card that will truly stand out. Nothing too busy. Simple is good, right? Not looking for a standard design either. No cookie cutter layout. We are a Travel Company that works more with Companies than Travelers. I had an idea to focus and emphasis on the 2 logo a bit more. This is not necessary, however thought it would look interesting. I am just looking for something interesting and a bit different. Does't have to completely off the wall crazy, just not your run of the mill business card.

Target Market(s)

Hoteliers, Resort Management, Call Centers, Executives, Travelers, Families, Businesses

Industry/Entity Type

Hospitality

Contact Information for Business Card

President/CEO - Marco T Villena (title not necessary if design doesn't allow for it)
contact - (407) 555-0182
email - mvillena@roam4ward.example
address - 4127 Brindle Oak Way #164
Fernvale, ZZ 32899
website - www.roam4ward.example

Font styles to use
Serif
Other font styles liked:
• Avenir Next LT Pro BOLD

Requirements
Must have
• simple look and design. Unique design
Nice to have
• I attached the 2 logo separate from the main logo. This can be used separately from the Main Logo, together with the main logo or as main logo. I included the logo font. Use it or not, designers choice.
Should not have
• cookie cutter design. Little use of red other than the logo

```html
<!DOCTYPE html>
<html lang="en">
<head>
<meta charset="utf-8">
<title>roam4ward – Business Card</title>
<link rel="stylesheet" href="https://fonts.googleapis.com/css2?family=Montserrat:wght@300;400;500;800&display=swap">
<style>
  :root {
    --stage: #e6e6e6;
    --card: #ffffff;
    --pattern-light: #fbfbfb;
    --pattern-mid: #eeeeee;
    --ink: #111111;
    --ink-soft: #2b2b2b;
    --red: #ff0000;
    --white: #ffffff;
  }
  * { box-sizing: border-box; margin: 0; padding: 0; }
  html, body {
    width: 1200px;
    height: 1200px;
    overflow: hidden;
    background: var(--stage);
    font-family: "Montserrat", sans-serif;
  }
  .canvas { position: relative; width: 1200px; height: 1200px; }
  .card {
    position: absolute;
    left: 180px;
    width: 840px;
    height: 480px;
    background: var(--card);
    overflow: hidden;
    box-shadow: 0 10px 30px rgba(0,0,0,0.12);
  }
  .card--front { top: 70px; }
  .card--back { top: 640px; }

  .travel-pattern {
    position: absolute;
    inset: 0;
    background:
      radial-gradient(circle at 30% 40%, var(--pattern-light) 0%, transparent 60%),
      linear-gradient(135deg, var(--pattern-mid) 0%, var(--pattern-light) 50%, var(--pattern-mid) 100%);
  }

  /* Front */
  .brand-front {
    position: absolute;
    left: 0; right: 0;
    top: 190px;
    display: flex;
    align-items: center;
    justify-content: center;
    gap: 18px;
  }
  .brand-front__name {
    font-weight: 800;
    font-size: 66px;
    letter-spacing: -2px;
    color: var(--ink);
    line-height: 1;
  }
  .brand-dot { display: block; border-radius: 50%; background: var(--red); }
  .brand-front .brand-dot { width: 40px; height: 40px; }

  /* Back */
  .brand-back {
    position: absolute;
    left: 30px;
    top: 70px;
    width: 320px;
    display: flex;
    flex-direction: column;
    align-items: center;
    gap: 26px;
  }
  .brand-back .brand-dot { width: 200px; height: 200px; }
  .brand-back__name {
    font-weight: 800;
    font-size: 46px;
    letter-spacing: -1.5px;
    color: var(--ink);
    line-height: 1;
  }

  .info-frame { position: absolute; inset: 0; width: 840px; height: 480px; }

  .contact-name {
    position: absolute;
    left: 420px;
    top: 100px;
    font-weight: 300;
    font-size: 37px;
    color: var(--ink);
    line-height: 1;
    white-space: nowrap;
  }
  .contact-name__initial { color: var(--red); }

  .contact-title {
    position: absolute;
    left: 420px;
    top: 148px;
    width: 266px;
    height: 21px;
    background: var(--red);
    color: var(--white);
    font-size: 15px;
    font-weight: 400;
    line-height: 21px;
    padding-left: 16px;
  }

  .contact-list {
    position: absolute;
    left: 424px;
    top: 212px;
    list-style: none;
    font-size: 15px;
    color: var(--ink-soft);
    line-height: 1.25;
  }
  .contact-list__item { display: flex; align-items: center; gap: 12px; }
  .contact-list__item--address { margin-bottom: 26px; }
  .contact-list__item--phone { margin-bottom: 10px; }
  .contact-list__item--email { margin-bottom: 24px; }
  .contact-icon { width: 18px; height: 18px; flex: none; }
</style>
</head>
<body>
<main class="canvas">

  <section class="card card--front" aria-label="Business card front">
    <div class="travel-pattern" role="img" aria-label="Light grey hand-drawn travel doodle pattern: planes, suitcases, palm trees, globes, cars and landmarks"></div>
    <div class="brand-front">
      <span class="brand-front__name">roam4ward</span>
      <span class="brand-dot"></span>
    </div>
  </section>

  <section class="card card--back" aria-label="Business card back">
    <div class="travel-pattern" role="img" aria-label="Light grey hand-drawn travel doodle pattern: planes, suitcases, palm trees, globes, cars and landmarks"></div>

    <div class="brand-back">
      <span class="brand-dot"></span>
      <span class="brand-back__name">roam4ward</span>
    </div>

    <svg class="info-frame" viewBox="0 0 840 480" aria-hidden="true">
      <polyline points="343,88 399,88 399,403 683,403 683,434" fill="none" stroke="#111" stroke-width="1.6"/>
    </svg>

    <h1 class="contact-name">Marco <span class="contact-name__initial">T</span> Villena</h1>
    <p class="contact-title">President/CEO</p>

    <ul class="contact-list">
      <li class="contact-list__item contact-list__item--address">
        <svg class="contact-icon" viewBox="0 0 24 24"><path d="M12 2a7 7 0 0 0-7 7c0 5 7 13 7 13s7-8 7-13a7 7 0 0 0-7-7zm0 9.5A2.5 2.5 0 1 1 12 6.5a2.5 2.5 0 0 1 0 5z" fill="#111"/></svg>
        <span>4127 Brindle Oak Way #164<br>Fernvale, ZZ 32899</span>
      </li>
      <li class="contact-list__item contact-list__item--phone">
        <svg class="contact-icon" viewBox="0 0 24 24"><path d="M6.6 10.8a15 15 0 0 0 6.6 6.6l2.2-2.2a1 1 0 0 1 1-.25 11.4 11.4 0 0 0 3.6.57 1 1 0 0 1 1 1V20a1 1 0 0 1-1 1A17 17 0 0 1 3 4a1 1 0 0 1 1-1h3.5a1 1 0 0 1 1 1c0 1.25.2 2.45.57 3.57a1 1 0 0 1-.25 1z" fill="#111"/></svg>
        <span>(555) 555-0182</span>
      </li>
      <li class="contact-list__item contact-list__item--email">
        <svg class="contact-icon" viewBox="0 0 24 24"><path d="M2 5h20v14H2z" fill="#111"/><path d="M2 5l10 8 10-8" fill="none" stroke="#fff" stroke-width="1.6"/></svg>
        <span>mvillena@roam4ward.example</span>
      </li>
      <li class="contact-list__item contact-list__item--web">
        <svg class="contact-icon" viewBox="0 0 24 24"><circle cx="12" cy="12" r="9" fill="none" stroke="#111" stroke-width="2"/><ellipse cx="12" cy="12" rx="4" ry="9" fill="none" stroke="#111" stroke-width="1.6"/><path d="M3 12h18" stroke="#111" stroke-width="1.6"/></svg>
        <span>www.roam4ward.example</span>
      </li>
    </ul>
  </section>

</main>
</body>
</html>
```